*YO!!! Designers Needed...Again!!* 1 Page Cover Needed for a $$Billion Dollar$$ Company (Contest)

After 2 successful projects on SketchHarbor, we're back again and need YOUR help! Last time we needed a front page cover for our annual report. This time we're seeking one for our annual catalog.

We are a manufacturer of aluminum electrolytic capacitors. We are a publicly listed company and work with many Fortune 500 companies, so your work will be viewed by the BIG GUNS and EXECUTIVES around the WORLD! If selected, you may be selected for additional work. The catalog will be distributed to all of our clients as well as be distributed at major trade shows in 2021 and 2022.

The cover should be unique. If colorful, modern, artistic, and creativity somehow got together and had a child, that's what the cover page would look like!

Inspired Examples attached. Check them out!

www.velmor-parts.example

Target Market(s)

Consumers, Purchasers, Engineers

Industry/Entity Type

Electronic

Font styles to use
Sans Serif

Requirements
Must have
• 1. Must include the attached Velmor logo. Logo size, color, and placement are at your discretion.

2. Include the text, 'Aluminum Electrolytic Capacitors' (upper case or lower case is up to you) '2021/22'

3. Shall be in A4 size and vertical orientation.
Nice to have
• Feel free to add any icons or stock photos (for example capacitors or circuit boards) if needed. For ones requiring payments, add the stock graphic example and if we like it, provide the link/source and we will pay for it.

Feel free to use any of the capacitor icon attachments if you think it will help. These are optional and not required. Can photoshop as needed.

Be creative here and don't be afraid to be bold! The end product will be printed into a physical catalog.

Our slogan is "Think Ahead". This slogan can or cannot be part of the theme.

```html
<!DOCTYPE html>
<html lang="en">
<head>
<meta charset="utf-8">
<title>Velmor Catalog Cover 2021-22</title>
<link rel="stylesheet" href="https://fonts.googleapis.com/css2?family=Lato:wght@300;400;700;900&display=swap">
<style>
  :root {
    --backdrop: #8f8f8f;
    --cover: #0b0b0c;
    --white: #ffffff;
    --grey: #8a8a8a;
    --rule-grey: #7a7a7a;
    --url-grey: #9a9a9a;
  }
  * { margin: 0; padding: 0; box-sizing: border-box; }
  html, body {
    width: 1034px;
    height: 1200px;
    overflow: hidden;
    background: var(--backdrop);
    font-family: "Lato", sans-serif;
  }
  .cover {
    position: absolute;
    left: 107px;
    top: 20px;
    width: 820px;
    height: 1160px;
    background: var(--cover);
    color: var(--white);
    overflow: hidden;
  }
  .brand-name {
    position: absolute;
    left: 71px;
    top: 66px;
    font-weight: 700;
    font-size: 84px;
    line-height: 1;
    letter-spacing: -1px;
    color: var(--white);
  }
  .side-bar {
    position: absolute;
    left: 755px;
    top: 0;
    width: 11px;
    height: 46px;
    background: var(--white);
  }
  .side-url {
    position: absolute;
    left: 752px;
    top: 56px;
    writing-mode: vertical-rl;
    transform: rotate(180deg);
    font-size: 14px;
    font-weight: 400;
    color: var(--url-grey);
    letter-spacing: 0.3px;
  }
  .circuit-hand {
    position: absolute;
    left: 181px;
    top: 210px;
    width: 610px;
    height: 950px;
    background:
      radial-gradient(ellipse 45% 30% at 20% 55%, rgba(47,196,214,0.85), transparent 70%),
      radial-gradient(ellipse 40% 40% at 85% 35%, rgba(240,25,79,0.85), transparent 70%),
      radial-gradient(ellipse 35% 35% at 55% 25%, rgba(226,58,168,0.8), transparent 70%),
      radial-gradient(ellipse 30% 35% at 62% 88%, rgba(246,195,21,0.8), transparent 70%),
      radial-gradient(ellipse 25% 30% at 50% 70%, rgba(197,138,230,0.6), transparent 70%);
    opacity: 0.55;
  }
  .title {
    position: absolute;
    left: 73px;
    top: 783px;
    font-size: 42px;
    line-height: 46px;
    letter-spacing: -0.3px;
  }
  .title-light { font-weight: 300; color: var(--white); display: block; }
  .title-grey { font-weight: 700; color: var(--grey); display: block; }
  .title-bold { font-weight: 900; color: var(--white); display: block; }
  .title-rule {
    position: absolute;
    left: 73px;
    top: 937px;
    width: 288px;
    height: 4px;
    background: linear-gradient(to right, var(--rule-grey) 0 50%, var(--white) 50% 100%);
  }
  .edition {
    position: absolute;
    left: 74px;
    top: 948px;
    font-size: 38px;
    font-weight: 700;
    line-height: 1;
    color: var(--grey);
  }
  .edition-strong { color: var(--white); }
  .statement {
    position: absolute;
    left: 73px;
    top: 1016px;
    width: 310px;
    font-size: 13px;
    line-height: 16px;
    font-weight: 400;
    white-space: nowrap;
  }
  .statement strong { font-weight: 700; }
</style>
</head>
<body>
  <main class="cover">
    <div class="side-bar"></div>
    <div class="side-url">www.velmor-parts.example</div>

    <header class="brand">
      <div class="brand-name">Velmor</div>
    </header>

    <div class="circuit-hand" role="img" aria-label="Illustration of a raised hand built from colourful circuit-board traces, cyan on the thumb, violet and magenta across the fingers, red on the little finger and orange-yellow traces running down the wrist"></div>

    <h1 class="title">
      <span class="title-light">ALUMINUM</span>
      <span class="title-grey">ELECTROLYTIC</span>
      <span class="title-bold">CAPACITORS</span>
    </h1>
    <div class="title-rule"></div>
    <div class="edition"><span class="edition-strong">20</span>21-22</div>

    <p class="statement">We are a publicly listed company and work with<br>many Fortune 500 companies, so your work will be<br>viewed by the <strong>BIG GUNS and EXECUTIVES</strong><br><strong>around the WORLD!</strong></p>
  </main>
</body>
</html>
```